Tarek & Lubna's 50th Anniversary Celebration & Reunion

I need a flyer to send out via email and for posting on chatterboard to invite guests to a 50th wedding anniversary / family reunion.

Location is sunny La Jolla CA the Pearl of San Diego's Shore.

Week long daily activities starting Mon July 28-Aug 1st Friday, The event will be on Wednesday.
* Daily Catered Family Breakfast at the Marlow Hall of La Jolla
* Daily group activities including
*Exploring La Jolla Beaches & Ocean Cave Kayaking
*TideRealm Private Behind the Scenes Tour
*World Famous Pellham Wildlife Park
*Sunset Balloon Ride
*Private Yatch on the Bay

Actual Anniversary event will take place Thursday December 28, 2013 at 5pm at the Marlow Hall.

There are many local hotels around the Marlow Hall. 4213 Brindle Ln, La Jolla, CA 92058

Host is Kamil and the entire Haddour Family. For questions, please email Kamil@thelinden-feasts.com

Target Market(s)

all ages from 10 year olds to 70 year olds. Should appeal to all

Industry/Entity Type

Wedding

Font styles to use
Script

Colors

Designer to choose colors to be used in the design.

Requirements
Must have
• Fun graphics, including one with a stretch limo as there will be one available

Photo enclosed
Nice to have
• Logo for TideRealm Inserting a picture of an actual wedding 50 years ago or so of the bride and groom. incorporating the limo cropped out of the picture attached would also be nice

```html
<!DOCTYPE html>
<html lang="en">
<head>
<meta charset="utf-8">
<title>Tarek &amp; Lubna 50th Anniversary Flyer</title>
<link rel="stylesheet" href="https://fonts.googleapis.com/css2?family=Oswald:wght@300;400;500&family=Courgette&display=swap">
<style>
  :root {
    --page-bg: #1b1b1b;
    --flyer-dark: #262522;
    --flyer-mid: #3d3b35;
    --cream: #ece4c6;
    --gold: #d9cc98;
    --gold-deep: #b8a96e;
    --ink: #1e1d1a;
    --muted: #b9b29a;
  }
  * { box-sizing: border-box; margin: 0; padding: 0; }
  html, body { width: 1200px; height: 1028px; overflow: hidden; }
  body { background: var(--page-bg); display: flex; align-items: center; justify-content: center; }
  .flyer {
    width: 660px; height: 990px; position: relative; overflow: hidden;
    background: linear-gradient(160deg, var(--flyer-mid) 0%, var(--flyer-dark) 45%, #151513 100%);
    color: var(--cream); font-family: 'Oswald', sans-serif;
    box-shadow: 0 10px 40px rgba(0,0,0,.6);
  }
  .header { padding: 34px 40px 0; }
  .date-bar {
    display: inline-block; background: var(--gold); color: var(--ink);
    font-size: 38px; font-weight: 500; line-height: 1; padding: 4px 12px; letter-spacing: .5px;
  }
  .location { font-size: 22px; font-weight: 400; margin-top: 8px; }
  .coast { font-size: 58px; font-weight: 300; line-height: 1.05; color: var(--cream); letter-spacing: 1px; }
  .scene {
    position: absolute; left: 0; right: 0; top: 210px; height: 300px;
    background: linear-gradient(180deg, #4b4841 0%, #2c2b27 60%, #1d1c19 100%);
  }
  .limo {
    position: absolute; left: 30px; right: 30px; top: 40px; height: 220px;
    background: linear-gradient(90deg, #141412, #33322d 50%, #141412);
    border-radius: 18px;
  }
  .wedding-frame {
    position: absolute; left: 150px; top: 14px; width: 360px; height: 272px;
    border: 6px solid var(--gold); background: var(--gold);
    box-shadow: 0 4px 18px rgba(0,0,0,.6);
  }
  .wedding-photo {
    width: 100%; height: 100%;
    background: linear-gradient(135deg, #f1ecdc 0%, #bdb49b 45%, #4a463d 100%);
  }
  .activities { position: absolute; left: 40px; right: 40px; top: 530px; }
  .intro { font-size: 18px; letter-spacing: 1.5px; }
  .event-bar {
    display: inline-block; background: var(--gold); color: var(--ink);
    font-size: 30px; letter-spacing: 3px; padding: 2px 10px; margin-top: 4px; line-height: 1.15;
  }
  .activity-list { list-style: none; margin-top: 10px; font-family: 'Courgette', cursive; font-size: 20px; line-height: 1.4; }
  .activity-list li::before { content: "*"; }
  .footer { position: absolute; left: 40px; right: 40px; top: 820px; }
  .anniversary-box {
    border: 3px solid var(--gold); padding: 6px 12px; font-size: 18px; line-height: 1.3;
  }
  .hotels { font-size: 13px; color: var(--muted); margin-top: 10px; letter-spacing: .3px; }
  .more-info, .host { font-size: 27px; font-weight: 400; line-height: 1.15; letter-spacing: .5px; }
  .more-info { margin-top: 6px; }
</style>
</head>
<body>
  <article class="flyer">
    <header class="header">
      <div class="date-bar">MON JULY 28-AUG 1ST FRIDAY</div>
      <p class="location">Location is sunny La Jolla CA the Pearl of</p>
      <h1 class="coast">San Diego's Shore.</h1>
    </header>

    <section class="scene">
      <div class="limo" role="img" aria-label="Black stretch limousine with palm trees"></div>
      <div class="wedding-frame">
        <div class="wedding-photo" role="img" aria-label="Vintage wedding photo of the bride and groom"></div>
      </div>
    </section>

    <section class="activities">
      <p class="intro">Week long daily activities starting Mon July 28-Aug 1st Friday.</p>
      <div class="event-bar">The event will be on Wednesday.</div>
      <ul class="activity-list">
        <li>Daily Catered Family Breakfast at the Marlow Hall of La Jolla</li>
        <li>Daily group activities including</li>
        <li>Exploring La Jolla Beaches &amp; Ocean Cave Kayaking</li>
        <li>TideRealm Private Behind the Scenes Tour</li>
        <li>World Famous Pellham Wildlife Park</li>
        <li>Sunset Balloon Ride</li>
        <li>Private Yatch on the Bay</li>
      </ul>
    </section>

    <footer class="footer">
      <p class="anniversary-box">Actual Anniversary event will take place Thursday December 28, 2013 at 5pm at the Marlow Hall.</p>
      <p class="hotels">There are many local hotels around the Marlow Hall | 4213 Brindle Ln La Jolla | CA 92058</p>
      <p class="more-info">MORE INFO - EMAIL KAMIL@THELINDEN-FEASTS.COM</p>
      <p class="host">HOST IS KAMIL AND THE ENTIRE HADDOUR FAMILY</p>
    </footer>
  </article>
</body>
</html>
```